Summit Brightway Realty Group & Greenleaf Lending Services, Inc.
Present Our
Annual Holiday Celebration

for Agents, Originators, Clients & Friends
All are Welcome!!

Catered by Chef Ramo Ramo
w/ DJ and Full Dance Floor

** No Cover Charge
Saturday, January 22, 2022
7 pm - 11 pm

at Velvet Parlor
4871 Q Street NE Washington DC 20019

Call Marcus Pelletier at (240) 555-0184 with questions.

```html
<!DOCTYPE html>
<html lang="en">
<head>
<meta charset="utf-8">
<title>Annual Holiday Celebration</title>
<link href="https://fonts.googleapis.com/css2?family=Playfair+Display:wght@500;600&family=Great+Vibes&family=Lato:wght@400;700&display=swap" rel="stylesheet">
<style>
  :root {
    --page: #ffffff;
    --ink: #1f2533;
    --navy: #0f2544;
    --sky: #5fa6d3;
    --deep: #081426;
    --gold: #dcb272;
    --gold-line: #e2bd7e;
    --logo-teal: #1b7e86;
    --logo-blue: #1d4f9c;
  }
  * { margin: 0; padding: 0; box-sizing: border-box; }
  html, body { width: 1200px; height: 1195px; overflow: hidden; background: var(--page); }
  .canvas { position: relative; width: 1200px; height: 1195px; }
  .card {
    position: absolute; left: 170px; top: 158px; width: 865px; height: 867px; overflow: hidden;
  }
  .card-backdrop {
    position: absolute; inset: 0;
    background:
      radial-gradient(ellipse at 15% 10%, #8cc6e6 0%, transparent 45%),
      linear-gradient(150deg, var(--sky) 0%, #2f6fa5 35%, var(--navy) 70%, var(--deep) 100%);
  }
  .panel {
    position: absolute; left: 78px; top: 75px; width: 700px; height: 702px;
    background: #fff; border: 2px solid var(--gold-line);
  }
  .txt { position: absolute; white-space: nowrap; font-family: "Lato", Arial, sans-serif; color: var(--ink); }
  .center { left: 0; width: 1200px; text-align: center; }
  .brand {
    font-family: "Lato", Arial, sans-serif; font-weight: 700; font-size: 15px; line-height: 19px;
    text-transform: uppercase; letter-spacing: 0.5px;
  }
  .brand-realty { left: 318px; top: 296px; color: var(--logo-teal); }
  .brand-lending { left: 716px; top: 296px; color: var(--logo-blue); text-align: right; width: 150px; left: 716px; }
  .kicker { top: 388px; font-size: 19px; letter-spacing: 0.5px; }
  .kicker-rule { position: absolute; top: 398px; height: 1.5px; background: var(--gold-line); width: 91px; }
  .headline {
    top: 420px; font-family: "Playfair Display", Georgia, serif; font-weight: 600;
    font-size: 60px; letter-spacing: 1px; color: var(--ink); line-height: 70px;
  }
  .script {
    top: 468px; font-family: "Great Vibes", cursive; font-size: 84px; color: var(--gold); line-height: 100px;
  }
  .audience { font-size: 19px; letter-spacing: 2.2px; line-height: 25px; }
  .row-rule { position: absolute; left: 316px; width: 562px; height: 1.5px; background: var(--gold-line); }
  .chef-photo {
    position: absolute; left: 336px; top: 636px; width: 113px; height: 109px;
    border: 2px solid var(--gold-line);
    background: linear-gradient(160deg, #b9bdc4 0%, #8e939b 55%, #d8d4cc 100%);
  }
  .feature {
    left: 476px; font-family: "Playfair Display", Georgia, serif; font-weight: 500;
    font-size: 22px; letter-spacing: 0.3px; line-height: 27px; text-transform: uppercase;
  }
  .detail { font-size: 19px; letter-spacing: 2px; }
  .venue { top: 792px; font-weight: 700; font-size: 25px; letter-spacing: 2.5px; color: var(--gold); }
  .address { top: 823px; font-size: 20px; letter-spacing: 2.2px; }
  .contact { top: 877px; font-size: 16.5px; letter-spacing: 1.2px; }
</style>
</head>
<body>
<main class="canvas">
  <section class="card">
    <div class="card-backdrop" role="img" aria-label="Blue watercolor backdrop scattered with gold foil flecks"></div>
    <div class="panel"></div>
  </section>

  <div class="txt brand brand-realty">Summit Brightway<br>Realty Group</div>
  <div class="txt brand brand-lending">Greenleaf Lending<br>Services, Inc.</div>

  <div class="kicker-rule" style="left:417px"></div>
  <div class="kicker-rule" style="left:675px"></div>
  <p class="txt center kicker">PRESENT OUR</p>

  <h1 class="txt center headline">ANNUAL HOLIDAY</h1>
  <p class="txt center script" style="left:12px">Celebration</p>

  <p class="txt center audience" style="top:588px">FOR AGENTS, ORIGINATORS, CLIENTS &amp; FRIENDS</p>
  <p class="txt center audience" style="top:613px">ALL ARE WELCOME!!</p>

  <div class="row-rule" style="top:655px"></div>
  <div class="row-rule" style="top:721px"></div>
  <div class="chef-photo" role="img" aria-label="Portrait photo of the caterer"></div>
  <p class="txt feature" style="top:663px">Catered by Chef Ramo Ramo</p>
  <p class="txt feature" style="top:690px">W/ DJ and Full Dance Floor</p>

  <p class="txt detail" style="left:476px; top:735px">** NO COVER CHARGE</p>
  <p class="txt detail" style="left:528px; top:759px">7 PM - 11 PM</p>

  <p class="txt center venue">VELVET PARLOR</p>
  <p class="txt center address">4871 Q STREET NE WASHINGTON DC 20019</p>
  <p class="txt center contact">CALL MARCUS PELLETIER AT (240) 555-0184 WITH QUESTIONS.</p>
</main>
</body>
</html>
```